Edit current business card design

Need business card design where Business Name, Logo, Address, phone and fax, website address are permanent.Need to be able to add and edit employee name and email address.

Business

```html
<!DOCTYPE html>
<html lang="en">
<head>
<meta charset="utf-8">
<title>Marlowe's Accounting Services – Business Card</title>
<link rel="stylesheet" href="https://fonts.googleapis.com/css2?family=Montserrat:wght@600&family=Open+Sans:wght@400;600&display=swap">
<style>
  :root {
    --page-bg: #ecebe8;
    --card-bg: #ffffff;
    --brand-green: #2d5e45;
    --text-dark: #1f1f1f;
    --pattern-light: #f2f2f1;
    --pattern-mid: #e3e4e2;
    --card-shadow: rgba(0, 0, 0, 0.14);
  }
  * { margin: 0; padding: 0; box-sizing: border-box; }
  html, body {
    width: 1200px;
    height: 900px;
    overflow: hidden;
    background: var(--page-bg);
  }
  .stage {
    position: relative;
    width: 1200px;
    height: 900px;
  }
  .card {
    position: absolute;
    width: 630px;
    height: 360px;
    background: var(--card-bg);
    box-shadow: 0 6px 18px var(--card-shadow);
    overflow: hidden;
  }
  .card--back { left: 150px; top: 60px; }
  .card--front { left: 420px; top: 475px; }

  .back-pattern {
    position: absolute;
    inset: 0;
    background: radial-gradient(circle at 40% 40%, var(--pattern-mid), var(--pattern-light) 75%);
  }
  .back-brand {
    position: absolute;
    right: 40px;
    bottom: 48px;
    text-align: left;
  }
  .brand-name {
    font-family: "Montserrat", sans-serif;
    font-weight: 600;
    color: var(--brand-green);
    letter-spacing: 0.14em;
    line-height: 1;
  }
  .brand-tagline {
    font-family: "Open Sans", sans-serif;
    font-weight: 400;
    color: var(--brand-green);
    letter-spacing: 0.06em;
    margin-top: 4px;
  }
  .back-brand .brand-name { font-size: 30px; }
  .back-brand .brand-tagline { font-size: 15px; }

  .front-brand {
    position: absolute;
    left: 34px;
    top: 34px;
    display: flex;
    align-items: center;
    gap: 14px;
  }
  .brand-dot {
    width: 82px;
    height: 82px;
    border-radius: 50%;
    background: var(--brand-green);
    flex: none;
  }
  .front-brand .brand-name { font-size: 28px; }
  .front-brand .brand-tagline { font-size: 14px; }

  .contact {
    position: absolute;
    left: 395px;
    top: 140px;
    font-family: "Open Sans", sans-serif;
    color: var(--text-dark);
  }
  .contact__name {
    font-size: 17px;
    font-weight: 600;
    color: var(--brand-green);
    line-height: 1.1;
  }
  .contact__credentials {
    font-size: 12px;
    line-height: 1.3;
    margin-bottom: 16px;
  }
  .contact__address {
    font-size: 13.5px;
    line-height: 1.35;
    margin-bottom: 14px;
  }
  .contact__list { list-style: none; font-size: 13.5px; line-height: 1.35; }
  .contact__list li { display: flex; align-items: center; gap: 7px; }
  .contact__icon { width: 11px; height: 11px; fill: var(--text-dark); flex: none; }
</style>
</head>
<body>
<main class="stage">

  <section class="card card--back" aria-label="Card back">
    <div class="back-pattern" role="img" aria-label="Faint repeating brand monogram pattern across the card"></div>
    <div class="back-brand">
      <p class="brand-name">MARLOWE'S</p>
      <p class="brand-tagline">Accounting Services</p>
    </div>
  </section>

  <section class="card card--front" aria-label="Card front">
    <div class="front-brand">
      <span class="brand-dot" aria-hidden="true"></span>
      <div>
        <p class="brand-name">MARLOWE'S</p>
        <p class="brand-tagline">Accounting Services</p>
      </div>
    </div>

    <div class="contact">
      <p class="contact__name">Dana Marlowe</p>
      <p class="contact__credentials">EA,ATA,ATP</p>
      <p class="contact__address">12345, Address Goes Here<br>Country Name, 123456.</p>
      <ul class="contact__list">
        <li>
          <svg class="contact__icon" viewBox="0 0 24 24" aria-hidden="true"><path d="M6.6 10.8a15.1 15.1 0 0 0 6.6 6.6l2.2-2.2c.3-.3.7-.4 1-.2 1.1.4 2.3.6 3.6.6.6 0 1 .4 1 1V20c0 .6-.4 1-1 1A17 17 0 0 1 3 4c0-.6.4-1 1-1h3.5c.6 0 1 .4 1 1 0 1.3.2 2.5.6 3.6.1.3 0 .7-.2 1z"/></svg>
          044-123 456 789
        </li>
        <li>
          <svg class="contact__icon" viewBox="0 0 24 24" aria-hidden="true"><path d="M2 5h20v14H2z M2 5l10 8 10-8" fill="none" stroke="#1f1f1f" stroke-width="2.4"/></svg>
          info@marlowebooks.example
        </li>
        <li>
          <svg class="contact__icon" viewBox="0 0 24 24" aria-hidden="true"><path d="M10 14l4-4 M8.5 12.5l-3 3a3 3 0 0 0 4.2 4.2l3-3 M15.5 11.5l3-3a3 3 0 0 0-4.2-4.2l-3 3" fill="none" stroke="#1f1f1f" stroke-width="2.4" stroke-linecap="round"/></svg>
          www.marlowebooks.example
        </li>
      </ul>
    </div>
  </section>

</main>
</body>
</html>
```